Coastline Haven Retreats Business Card Design

Design a business card for Coastline Haven Retreats. Look at the website for colors and reference. Card should have logo, name, title, office number, mobile number, email, URL and a tagline like, "Luxury Hotel & Resort Email Marketing" (This might change).

https://www.coastlinehavenretreats.example

The rest I will leave up to your imagination.

Contact Information for Business Card

Logo, name, title, office number, mobile number, email, URL and a tagline like, "Luxury Hotel & Resort Email Marketing" (This might change).

```html
<!DOCTYPE html>
<html lang="en">
<head>
<meta charset="utf-8">
<title>Coastline Haven Retreats – Business Card</title>
<link rel="stylesheet" href="https://fonts.googleapis.com/css2?family=Open+Sans:wght@400;700&display=swap">
<style>
  :root {
    --backdrop: #222222;
    --card-dark: #1f1f22;
    --brand-orange: #f47421;
    --orange-deep: #d9611a;
    --text-light: #ffffff;
  }
  html, body {
    margin: 0;
    padding: 0;
    width: 1200px;
    height: 780px;
    overflow: hidden;
    background: var(--backdrop);
    font-family: "Open Sans", Arial, sans-serif;
  }
  .canvas {
    position: relative;
    width: 1200px;
    height: 780px;
  }
  .card {
    position: absolute;
    top: 240px;
    width: 525px;
    height: 300px;
    box-sizing: border-box;
  }
  .card--front {
    left: 50px;
    background: var(--card-dark);
    color: var(--text-light);
  }
  .card--back {
    left: 625px;
    background: var(--brand-orange);
    display: flex;
    align-items: center;
    justify-content: center;
  }
  .brand {
    position: absolute;
    top: 34px;
    left: 34px;
    display: flex;
    align-items: center;
    gap: 10px;
  }
  .brand__mark {
    width: 14px;
    height: 14px;
    background: var(--brand-orange);
  }
  .brand__name {
    font-weight: 700;
    font-size: 19px;
    letter-spacing: 0.5px;
    text-transform: uppercase;
    color: var(--text-light);
  }
  .tagline {
    position: absolute;
    top: 82px;
    left: 34px;
    margin: 0;
    font-size: 12.5px;
    line-height: 1.35;
    color: var(--brand-orange);
  }
  .contact {
    position: absolute;
    left: 34px;
    bottom: 30px;
    margin: 0;
    padding: 0;
    list-style: none;
    font-size: 12px;
    line-height: 1.55;
  }
  .contact li {
    display: flex;
    align-items: center;
    gap: 7px;
  }
  .contact svg {
    width: 11px;
    height: 11px;
    flex: none;
  }
  .person {
    position: absolute;
    right: 44px;
    top: 168px;
    text-align: right;
  }
  .person__name {
    margin: 0;
    font-weight: 700;
    font-size: 27px;
    line-height: 1.1;
    color: var(--text-light);
  }
  .person__first {
    color: var(--brand-orange);
  }
  .person__title {
    margin: 2px 0 0;
    font-size: 14px;
  }
  .edge-tab {
    position: absolute;
    right: 0;
    top: 210px;
    width: 24px;
    height: 44px;
    background: var(--brand-orange);
  }
  .back-name {
    font-weight: 700;
    font-size: 26px;
    letter-spacing: 1px;
    text-transform: uppercase;
    color: var(--orange-deep);
  }
</style>
</head>
<body>
<main class="canvas">
  <section class="card card--front" aria-label="Business card front">
    <div class="brand">
      <span class="brand__mark"></span>
      <span class="brand__name">Coastline Haven Retreats</span>
    </div>
    <p class="tagline">Luxury Hotel &amp;<br>Resort Email Marketing</p>

    <ul class="contact">
      <li>
        <svg viewBox="0 0 12 12" aria-hidden="true"><path d="M2.5 1 L4.5 1 L5.3 3.6 L4 4.6 Q5 6.8 7.4 8 L8.4 6.7 L11 7.5 L11 9.5 Q11 11 9.5 11 Q1 10 1 2.5 Q1 1 2.5 1 Z" fill="var(--brand-orange)"/></svg>
        (555) 014-2758
      </li>
      <li>
        <svg viewBox="0 0 12 12" aria-hidden="true"><rect x="3" y="1" width="6" height="10" rx="1" fill="none" stroke="var(--brand-orange)" stroke-width="1.2"/></svg>
        (555) 019-7777
      </li>
      <li>
        <svg viewBox="0 0 12 12" aria-hidden="true"><circle cx="6" cy="6" r="5" fill="none" stroke="var(--brand-orange)" stroke-width="1.2"/><path d="M1 6 H11 M6 1 Q3 6 6 11 M6 1 Q9 6 6 11" fill="none" stroke="var(--brand-orange)" stroke-width="1"/></svg>
        www.coastlinehavenretreats.example
      </li>
      <li>
        <svg viewBox="0 0 12 12" aria-hidden="true"><rect x="1" y="2.5" width="10" height="7" fill="none" stroke="var(--brand-orange)" stroke-width="1.2"/><path d="M1 2.5 L6 6.5 L11 2.5" fill="none" stroke="var(--brand-orange)" stroke-width="1.2"/></svg>
        info@coastlinehavenretreats.example
      </li>
    </ul>

    <div class="person">
      <p class="person__name"><span class="person__first">Marta</span> Kovalenko</p>
      <p class="person__title">Co-Founder</p>
    </div>
    <span class="edge-tab"></span>
  </section>

  <section class="card card--back" aria-label="Business card back">
    <span class="back-name">Coastline Haven Retreats</span>
  </section>
</main>
</body>
</html>
```